Personal Finance e-commerce website needs a simple budget design

Hello! I am starting to sell downloadable and printable budget planners, as shown in the attached file, for people to plan ahead on their personal finances. <br/><br/>I want to see a one-page design with similar columns (for example, "Expenses, Budget, and Actual"). I would also like to see the basic formula ("Net Income = Gross income - Total Expenses") somewhere on the design. Finally, I want the design to remain mostly minimalistic and simple for the average person to plan their personal monthly budgets.<br/><br/>However, other than that, the overall design, layout, and colors will be at the graphic designer's choice. If you have any questions for me, please let me know. Thank you for your time!

Industry/Entity Type

Financial Planning

Colors

Designer to choose colors to be used in the design.

Requirements
Must have
• I want to see a one-page design with similar columns (for example, "Expenses, Budget, and Actual").
• I want the design to remain mostly minimalistic and simple for the average person to plan their personal monthly budgets.
Nice to have
• I would also like to see the basic formula ("Net Income = Gross income - Total Expenses") somewhere on the design.

```html
<!DOCTYPE html>
<html lang="en">
<head>
<meta charset="utf-8">
<title>Basic Monthly Budget</title>
<link href="https://fonts.googleapis.com/css2?family=Open+Sans:wght@600;700&display=swap" rel="stylesheet">
<style>
  :root {
    --backdrop: #2a2a2a;
    --paper: #ffffff;
    --ink: #6b6b6b;
    --ink-soft: #8a8a8a;
    --rule: #c9c9c9;
    --row-plain: #f8f7f5;
    --exp-head: #ecdfdb;
    --exp-row: #f5ebe8;
    --exp-ink: #a08a86;
    --bud-head: #e6e7df;
    --bud-row: #eeeee7;
    --bud-ink: #8c8c80;
    --act-head: #e8e4f0;
    --act-row: #efedf6;
    --act-ink: #9a90b2;
    --total-exp: #eee0db;
    --total-ink: #b0806f;
    --net-fill: #e6e7df;
    --hint: #ece6e4;
  }
  * { margin: 0; padding: 0; box-sizing: border-box; }
  html, body { width: 1200px; height: 900px; overflow: hidden; }
  body {
    background: var(--backdrop);
    font-family: "Open Sans", Arial, sans-serif;
    position: relative;
  }
  .sheet {
    position: absolute;
    left: 295px; top: 55px;
    width: 611px; height: 791px;
    background: var(--paper);
  }
  .sheet-title {
    position: absolute;
    top: 30px; left: 0; width: 100%;
    text-align: center;
    font-size: 13px; font-weight: 700;
    color: var(--ink);
    letter-spacing: 0.2px;
  }
  .date-line {
    position: absolute;
    left: 208px; top: 83px;
    width: 194px; height: 1px;
    background: var(--rule);
  }
  .date-label {
    position: absolute; top: 93px;
    font-size: 9px; font-weight: 600;
    color: var(--ink-soft);
    transform: translateX(-50%);
  }
  .date-month { left: 258px; }
  .date-year { left: 358px; }

  .budget-table {
    position: absolute;
    left: 36px; top: 121px;
    width: 539px;
    display: grid;
    grid-template-columns: 269px 132px 133px;
    column-gap: 2.5px;
  }
  .cell { height: 32.4px; }
  .head {
    display: flex; align-items: center; justify-content: center;
    font-size: 10px; font-weight: 600;
    text-shadow: 0 0 2px #fff, 0 0 2px #fff;
  }
  .head-exp { background: var(--exp-head); color: var(--exp-ink); }
  .head-bud { background: var(--bud-head); color: var(--bud-ink); }
  .head-act { background: var(--act-head); color: var(--act-ink); }
  .hint {
    background: var(--row-plain);
    display: flex; align-items: center; justify-content: center;
    font-size: 8px; font-weight: 600;
    color: var(--hint);
    white-space: nowrap; overflow: hidden;
  }
  .row-exp { background: var(--exp-row); }
  .row-bud { background: var(--bud-row); }
  .row-act { background: var(--act-row); }
  .row-plain { background: var(--row-plain); }

  .formula {
    position: absolute;
    top: 705px; left: 36px; width: 539px;
    font-size: 10px; font-weight: 600;
    color: var(--bud-ink);
  }
  .formula span { position: absolute; transform: translateX(-50%); white-space: nowrap; }
  .f-net { left: 136px; }
  .f-eq { left: 230px; }
  .f-gross { left: 338px; }
  .f-minus { left: 405px; }
  .f-total { left: 472px; color: var(--total-ink); }

  .totals {
    position: absolute;
    top: 721px; left: 36px;
    width: 539px; height: 32px;
    display: grid;
    grid-template-columns: 269px 132px 133px;
    column-gap: 2.5px;
  }
  .total-net {
    background: var(--net-fill);
    clip-path: polygon(0 0, 100% 0, 100% 100%, 0 100%, 7px 50%);
  }
  .total-gross { background: var(--net-fill); }
  .total-exp { background: var(--total-exp); }
</style>
</head>
<body>
  <main class="sheet">
    <h1 class="sheet-title">BASIC MONTHLY BUDGET</h1>
    <div class="date-line"></div>
    <span class="date-label date-month">MONTH</span>
    <span class="date-label date-year">YEAR</span>

    <section class="budget-table">
      <div class="cell head head-exp">EXPENSES (CATEGORY)</div>
      <div class="cell head head-bud">BUDGET (USD $)</div>
      <div class="cell head head-act">ACTUAL (USD $)</div>

      <div class="cell hint">CUSTOM CATEGORY</div>
      <div class="cell hint">WHAT YOU PLAN TO SPEND</div>
      <div class="cell hint">WHAT YOU ACTUALLY SPENT</div>

      <div class="cell row-exp"></div><div class="cell row-bud"></div><div class="cell row-act"></div>
      <div class="cell row-plain"></div><div class="cell row-plain"></div><div class="cell row-plain"></div>
      <div class="cell row-exp"></div><div class="cell row-bud"></div><div class="cell row-act"></div>
      <div class="cell row-plain"></div><div class="cell row-plain"></div><div class="cell row-plain"></div>
      <div class="cell row-exp"></div><div class="cell row-bud"></div><div class="cell row-act"></div>
      <div class="cell row-plain"></div><div class="cell row-plain"></div><div class="cell row-plain"></div>
      <div class="cell row-exp"></div><div class="cell row-bud"></div><div class="cell row-act"></div>
      <div class="cell row-plain"></div><div class="cell row-plain"></div><div class="cell row-plain"></div>
      <div class="cell row-exp"></div><div class="cell row-bud"></div><div class="cell row-act"></div>
      <div class="cell row-plain"></div><div class="cell row-plain"></div><div class="cell row-plain"></div>
      <div class="cell row-exp"></div><div class="cell row-bud"></div><div class="cell row-act"></div>
      <div class="cell row-plain"></div><div class="cell row-plain"></div><div class="cell row-plain"></div>
      <div class="cell row-exp"></div><div class="cell row-bud"></div><div class="cell row-act"></div>
      <div class="cell row-plain"></div><div class="cell row-plain"></div><div class="cell row-plain"></div>
      <div class="cell row-exp"></div><div class="cell row-bud"></div><div class="cell row-act"></div>
      <div class="cell row-plain"></div><div class="cell row-plain"></div><div class="cell row-plain"></div>
    </section>

    <div class="formula">
      <span class="f-net">NET INCOME</span>
      <span class="f-eq">=</span>
      <span class="f-gross">GROSS INCOME</span>
      <span class="f-minus">—</span>
      <span class="f-total">TOTAL EXPENSES</span>
    </div>

    <div class="totals">
      <div class="total-net"></div>
      <div class="total-gross"></div>
      <div class="total-exp"></div>
    </div>
  </main>
</body>
</html>
```